I need a business card design for a new company that will be doing consulting work around issues of cultural competency, and diversity and inclusion. I would like the design to be crisp and clear with bold but conservative colors and incorporate shades of blue

Target Market(s)

Small businesses, schools, non-profits

Industry/Entity Type

Consulting

Font styles to use
Serif
Sans Serif

Colors
0c5ba6
6b449b
3276b5
0292cd

Requirements
Must have
• A Morrow Venture (name of company)
• Lemlem Tavish
• CEO
• lemlem@amorrowventure.com
• (215)483-2756

```html
<!DOCTYPE html>
<html lang="en">
<head>
<meta charset="utf-8">
<title>A Morrow Venture — Business Card</title>
<link rel="stylesheet" href="https://fonts.googleapis.com/css2?family=Poppins:ital,wght@0,600;1,700&family=Didact+Gothic&family=Oswald:wght@400&family=Fira+Sans+Condensed:wght@600&display=swap">
<style>
  :root {
    --purple: #6b449b;
    --purple-soft: #7a55a8;
    --teal-blue: #0292cd;
    --paper: #ffffff;
  }
  html, body {
    margin: 0;
    padding: 0;
    width: 1200px;
    height: 857px;
    overflow: hidden;
    background: var(--paper);
  }
  .card {
    position: relative;
    width: 1200px;
    height: 857px;
    background: var(--paper);
  }
  .contact {
    position: absolute;
    right: 43px;
    top: 36px;
    text-align: right;
    color: var(--purple);
  }
  .contact p { margin: 0; }
  .contact__name {
    font-family: "Poppins", sans-serif;
    font-weight: 600;
    font-size: 43px;
    line-height: 1;
    letter-spacing: 0.5px;
  }
  .contact__title {
    font-family: "Poppins", sans-serif;
    font-weight: 700;
    font-style: italic;
    font-size: 22px;
    line-height: 1;
    margin-top: 6px !important;
  }
  .contact__email,
  .contact__phone {
    font-family: "Didact Gothic", sans-serif;
    font-size: 34px;
    line-height: 1;
    color: var(--purple-soft);
    letter-spacing: 0.5px;
  }
  .contact__email { margin-top: 20px !important; }
  .contact__phone { margin-top: 22px !important; }

  .brand {
    position: absolute;
    left: 43px;
    top: 288px;
    width: 1114px;
    height: 257px;
    display: flex;
    align-items: center;
    justify-content: center;
    margin: 0;
    font-family: "Oswald", sans-serif;
    font-weight: 400;
    font-size: 113px;
    letter-spacing: 2px;
    color: var(--purple);
  }

  .services {
    position: absolute;
    left: 48px;
    top: 590px;
    list-style: none;
    margin: 0;
    padding: 0;
  }
  .services__item {
    display: flex;
    align-items: center;
    height: 76px;
    font-family: "Fira Sans Condensed", sans-serif;
    font-weight: 600;
    font-size: 44px;
    color: var(--teal-blue);
  }
  .services__marker {
    width: 17px;
    height: 34px;
    margin-right: 21px;
    flex: none;
  }
</style>
</head>
<body>
<main class="card">
  <header class="contact">
    <p class="contact__name">Lemlem Tavish</p>
    <p class="contact__title">CEO</p>
    <p class="contact__email">lemlem@amorrowventure.com</p>
    <p class="contact__phone">215-483-2756</p>
  </header>

  <h1 class="brand">A Morrow Venture</h1>

  <ul class="services">
    <li class="services__item">
      <svg class="services__marker" viewBox="0 0 17 34" aria-hidden="true"><path d="M17 0 A17 17 0 0 0 17 34 Z" fill="var(--purple)"/></svg>
      Cultural Competency
    </li>
    <li class="services__item">
      <svg class="services__marker" viewBox="0 0 17 34" aria-hidden="true"><path d="M17 0 A17 17 0 0 0 17 34 Z" fill="var(--purple)"/></svg>
      Diversity
    </li>
    <li class="services__item">
      <svg class="services__marker" viewBox="0 0 17 34" aria-hidden="true"><path d="M17 0 A17 17 0 0 0 17 34 Z" fill="var(--purple)"/></svg>
      Inclusion
    </li>
  </ul>
</main>
</body>
</html>
```